Moravel Stenwick Inc needs a business card design

Looking for a unique, classy and sharp business card design.

Contact Information for Business Card

Moravel Stenwick Inc.
Marisa Ortega Bellido BScOT(c)
Occupational Therapist
(780) 555-0142
moravelstenwick@postlynx.net

```html
<!DOCTYPE html>
<html lang="en">
<head>
<meta charset="utf-8">
<title>Moravel Stenwick Inc. — Business Card</title>
<link href="https://fonts.googleapis.com/css2?family=Open+Sans:wght@300;400;600&display=swap" rel="stylesheet">
<style>
  :root {
    --page-bg: #e9e6e2;
    --purple-light: #b554bd;
    --purple-dark: #8c2590;
    --card-white: #f7f7f7;
    --name-blue: #2aa6df;
    --title-white: #f4e9f6;
    --icon-green: #8cc63f;
    --contact-grey: #8a8a8a;
    --brand-purple: #9b3aa0;
  }
  * { box-sizing: border-box; margin: 0; padding: 0; }
  html, body {
    width: 1200px;
    height: 1022px;
    overflow: hidden;
    background: var(--page-bg);
    font-family: "Open Sans", Arial, sans-serif;
  }
  .stage {
    width: 1200px;
    height: 1022px;
    display: flex;
    align-items: center;
    justify-content: center;
  }
  .business-card {
    position: relative;
    width: 900px;
    height: 514px;
    display: flex;
    background: var(--card-white);
    box-shadow: 0 14px 40px rgba(0,0,0,0.18);
    overflow: hidden;
  }
  .identity-band {
    position: relative;
    width: 330px;
    height: 100%;
    background: linear-gradient(160deg, var(--purple-dark) 0%, var(--purple-light) 55%, var(--purple-dark) 100%);
  }
  .identity-text {
    position: absolute;
    left: 40px;
    right: 20px;
    bottom: 62px;
  }
  .person-name {
    color: var(--name-blue);
    font-weight: 600;
    font-size: 25px;
    line-height: 1.2;
  }
  .person-credential {
    color: var(--title-white);
    font-weight: 300;
    font-size: 20px;
  }
  .person-title {
    color: var(--title-white);
    font-weight: 300;
    font-size: 21px;
    margin-top: 6px;
  }
  .info-panel {
    position: relative;
    flex: 1;
  }
  .brand-mark {
    position: absolute;
    right: 56px;
    top: 190px;
    display: flex;
    align-items: center;
    gap: 14px;
  }
  .brand-dot {
    width: 22px;
    height: 22px;
    border-radius: 50%;
    background: var(--icon-green);
  }
  .brand-name {
    color: var(--brand-purple);
    font-weight: 600;
    font-size: 36px;
    letter-spacing: -0.5px;
  }
  .contact-list {
    position: absolute;
    left: 44px;
    bottom: 62px;
    list-style: none;
  }
  .contact-item {
    display: flex;
    align-items: center;
    gap: 16px;
    color: var(--contact-grey);
    font-weight: 300;
    font-size: 21px;
    line-height: 1.9;
  }
  .contact-icon { width: 16px; height: 16px; flex: none; }
</style>
</head>
<body>
<main class="stage">
  <section class="business-card">
    <div class="identity-band">
      <div class="identity-text">
        <p class="person-name">Marisa Ortega Bellido <span class="person-credential">BScOT(c)</span></p>
        <p class="person-title">Occupational Therapist</p>
      </div>
    </div>
    <div class="info-panel">
      <div class="brand-mark">
        <span class="brand-dot"></span>
        <span class="brand-name">Moravel Stenwick Inc.</span>
      </div>
      <ul class="contact-list">
        <li class="contact-item">
          <svg class="contact-icon" viewBox="0 0 16 16" aria-hidden="true">
            <path d="M4 1 L6.5 4 L5 6 Q6.5 9.5 10 11 L12 9.5 L15 12 L13 15 Q4 14 1 3 Z" fill="var(--icon-green)"/>
          </svg>
          <span>(780) 555-0142</span>
        </li>
        <li class="contact-item">
          <svg class="contact-icon" viewBox="0 0 16 16" aria-hidden="true">
            <rect x="1" y="3" width="14" height="10" fill="var(--icon-green)"/>
            <path d="M1 3 L8 9 L15 3" fill="none" stroke="#ffffff" stroke-width="1.2"/>
          </svg>
          <span>moravelstenwick@postlynx.net</span>
        </li>
      </ul>
    </div>
  </section>
</main>
</body>
</html>
```